Label for a new skin care product

Hello, we are launching a new skin care product. It's a face serum. One product only. I have attached the size requirements and a very general look at what is required. The final result will be a label sticker than gets placed on the bottle.

I have created some (amateur) designs using Canva here: https://www.plorvix.com/design/KTWmbHaxq3P/rQyTnnLoUsd_-JkZ_7_Xd_q/view?utm_content=KTWmbHaxq3P&utm_campaign=designshare&utm_medium=link2&utm_source=sharebutton

The text is what is required on the label. The design we are seeking is a very simply Wordmark logo with interesting font only. You can see I'm seeking ideas on a colorful design as well as something more ordinary/clinical. The people who will buy this product will be more upper class, well paid, and critical thinkers. Upscale. We don't want too many colors due to printing costs.

Target Market(s)

Female 25-45 years old who are hip and savvy

Requirements
Must have
• wordmark logo

```html
<!DOCTYPE html>
<html lang="en">
<head>
<meta charset="utf-8">
<title>Bloomi Skin – Snail Mucin Label</title>
<link rel="stylesheet" href="https://fonts.googleapis.com/css2?family=Tenor+Sans&family=Quicksand:wght@400;500;700&family=Noto+Sans+KR:wght@400;500&display=swap">
<style>
  :root {
    --page: #f0e2e3;
    --ink: #151515;
    --ink-soft: #2a2a2a;
    --coral: #ee7f80;
    --blush: #f9dfe4;
    --petal: #f6c9d0;
    --white: #ffffff;
  }
  * { margin: 0; padding: 0; box-sizing: border-box; }
  html, body { width: 1200px; height: 2230px; overflow: hidden; }
  body {
    background: var(--page);
    font-family: "Quicksand", sans-serif;
    color: var(--ink);
    position: relative;
  }

  /* ---------- Label ---------- */
  .label {
    position: absolute;
    left: 50px; top: 300px;
    width: 1100px; height: 720px;
    background: linear-gradient(180deg, var(--white) 0%, var(--white) 45%, #fdf1f3 62%, var(--blush) 100%);
    overflow: hidden;
  }
  .bloom {
    position: absolute;
    border-radius: 50%;
  }
  .bloom--top {
    left: 330px; top: -90px; width: 500px; height: 300px;
    background: radial-gradient(ellipse at center, rgba(246,190,200,.75) 0%, rgba(248,210,217,.5) 45%, rgba(255,255,255,0) 72%);
  }
  .bloom--left {
    left: -90px; top: 310px; width: 300px; height: 300px;
    background: radial-gradient(circle at center, rgba(246,196,205,.8) 0%, rgba(248,214,220,.45) 50%, rgba(255,255,255,0) 72%);
  }
  .bloom--right {
    right: -40px; top: 90px; width: 110px; height: 110px;
    background: radial-gradient(circle at center, rgba(244,188,198,.75) 0%, rgba(255,255,255,0) 70%);
  }
  .bloom--petal {
    right: -20px; top: 490px; width: 60px; height: 50px;
    background: radial-gradient(circle at center, rgba(240,150,160,.7) 0%, rgba(255,255,255,0) 70%);
  }

  .col {
    position: absolute;
    top: 0; height: 100%;
    text-align: center;
  }
  .col--left  { left: 56px;  width: 220px; }
  .col--mid   { left: 320px; width: 460px; }
  .col--right { left: 800px; width: 250px; }

  .block { position: absolute; left: 0; right: 0; }

  .heading {
    font-weight: 700;
    font-size: 15px;
    letter-spacing: .3px;
  }
  .copy {
    font-size: 15.5px;
    line-height: 19.5px;
    color: var(--ink-soft);
  }
  .copy strong { font-weight: 700; color: var(--ink); }

  .divider {
    position: absolute;
    height: 1.5px;
    background: var(--coral);
  }
  .divider::after {
    content: "";
    position: absolute;
    left: 50%; top: 50%;
    width: 7px; height: 7px;
    background: var(--coral);
    border-radius: 50%;
    transform: translate(-50%, -50%);
  }

  .brand-name {
    font-family: "Tenor Sans", sans-serif;
    font-size: 40px;
    color: var(--ink);
    letter-spacing: -.5px;
  }
  .title {
    font-family: "Tenor Sans", sans-serif;
    font-size: 76px;
    line-height: 62px;
    letter-spacing: -1px;
  }
  .strength {
    font-family: "Tenor Sans", sans-serif;
    font-size: 68px;
    line-height: 68px;
  }
  .subtitle {
    font-size: 24px;
    line-height: 28px;
    color: var(--coral);
    letter-spacing: .5px;
    text-transform: uppercase;
  }
  .claims { font-size: 16.5px; line-height: 19px; color: var(--ink-soft); }
  .korean {
    font-family: "Noto Sans KR", sans-serif;
    color: var(--ink-soft);
  }

  .icons {
    position: absolute;
    left: 0; right: 0; top: 565px;
    display: flex; justify-content: space-between; align-items: flex-start;
    padding: 0 8px 0 30px;
  }
  .icon-pet { text-align: center; font-size: 12px; font-weight: 700; }
  .volume { font-size: 14px; font-family: "Tenor Sans", sans-serif; }

  .social {
    display: flex; justify-content: center; align-items: center; gap: 8px;
    font-size: 14.5px;
  }
  .social-dot {
    width: 12px; height: 12px; border: 1.5px solid var(--ink-soft); border-radius: 50%;
  }
  .distributor { font-size: 11.5px; color: var(--ink-soft); }

  /* ---------- Wordmark options ---------- */
  .wordmarks {
    position: absolute;
    left: 115px; top: 1130px;
    width: 975px;
  }
  .wordmarks__title {
    text-align: center;
    font-size: 27px;
    font-weight: 500;
    margin-bottom: 28px;
  }
  .wordmarks__rule { height: 1px; background: var(--ink); }
  .wordmarks__grid {
    display: grid;
    grid-template-columns: repeat(3, 1fr);
    padding: 40px 0 50px;
  }
  .option { text-align: center; }
  .mark {
    height: 130px;
    position: relative;
    font-family: "Tenor Sans", sans-serif;
    color: var(--ink);
  }
  .mark__name { font-size: 64px; letter-spacing: -1px; line-height: 1; }
  .mark__reg { font-size: 26px; vertical-align: top; }
  .mark__sub { font-size: 30px; line-height: 1; }
  .mark--inline-right .mark__sub { position: absolute; right: 18px; top: 58px; }
  .mark--inline-left  .mark__sub { position: absolute; left: 40px; top: 58px; }
  .mark--stacked      .mark__sub { display: block; margin-top: 10px; }
  .mark--inline-right .mark__name,
  .mark--inline-left  .mark__name { padding-top: 6px; }
  .option__caption { font-size: 22px; margin-top: 24px; }
</style>
</head>
<body>

<section class="label" aria-label="Bottle label, unrolled">
  <div class="bloom bloom--top" role="img" aria-label="Soft pink blossom illustration behind the brand name"></div>
  <div class="bloom bloom--left" role="img" aria-label="Pink blossom illustration at the left edge"></div>
  <div class="bloom bloom--right" role="img" aria-label="Small pink blossom at the right edge"></div>
  <div class="bloom bloom--petal" role="img" aria-label="Single drifting petal"></div>

  <!-- Left panel -->
  <div class="col col--left">
    <p class="block heading" style="top:76px">SNAIL MUCIN ESSENCE</p>
    <p class="block copy" style="top:120px"><strong>Directions:</strong> For a pretty, natural glow apply AM and PM to freshly cleansed face, before all other actives.</p>
    <div class="divider" style="left:0;right:0;top:248px"></div>
    <p class="block copy" style="top:276px"><strong>Caution:</strong> External use only. Do not get into your eyes</p>

    <div class="icons">
      <svg width="52" height="52" viewBox="0 0 52 52" aria-label="12 months after opening">
        <path d="M5 10 L46 3 L47 9 L6 16 Z" fill="var(--ink)"/>
        <path d="M6 18 H46 V44 Q26 50 6 44 Z" fill="var(--ink)"/>
        <text x="26" y="40" text-anchor="middle" font-family="Quicksand, sans-serif" font-weight="700" font-size="14" fill="#fff">12M</text>
      </svg>
      <div class="icon-pet">
        <svg width="44" height="40" viewBox="0 0 44 40" aria-label="Recyclable">
          <path d="M22 4 L39 34 H5 Z" fill="none" stroke="var(--ink)" stroke-width="6" stroke-linejoin="round"/>
        </svg>
        <div>PET</div>
      </div>
      <svg width="46" height="46" viewBox="0 0 46 46" aria-label="Vegan">
        <path d="M8 40 C6 22 18 8 42 6 C42 28 30 40 12 38 Z" fill="var(--ink)"/>
        <path d="M8 40 L30 18" stroke="#fff" stroke-width="2.5" stroke-linecap="round"/>
      </svg>
    </div>
    <p class="block volume" style="top:660px">100 mL / 3.38 fl.oz</p>
  </div>

  <!-- Centre panel -->
  <div class="col col--mid">
    <p class="block brand-name" style="top:48px">bloomi<span style="font-size:18px"> skin</span></p>
    <h1 class="block title" style="top:218px">SNAIL<br>MUCIN</h1>
    <p class="block strength" style="top:364px">96%</p>
    <div class="divider" style="left:120px;right:120px;top:445px"></div>
    <p class="block subtitle" style="top:462px">Power Essence<br>With Gotu Kola</p>
    <div class="divider" style="left:118px;right:118px;top:532px"></div>
    <p class="block claims" style="top:556px">Paraben,Alcohol,Fragrance,<br>Phthalate,and Cruelty Free</p>
    <p class="block korean" style="top:647px;font-size:22px">뛰어난 수분 공급</p>
  </div>

  <!-- Right panel -->
  <div class="col col--right">
    <p class="block heading" style="top:76px">KEY INGREDIENTS</p>
    <p class="block copy" style="top:106px"><strong>Snail Mucin 96%</strong><br>Secretion Filtrate &amp;<br>Gotu Kola</p>
    <div class="divider" style="left:18px;right:28px;top:195px"></div>
    <p class="block copy" style="top:228px">Help provide all day hydration. It also helps repair damage, rebalance and prepare the skin for deeper absorption of serums and moisturizers.</p>
    <p class="block korean" style="top:390px;font-size:15.5px;line-height:19px">피부 보습, 다크 스팟 복구, 손상된 피부 재생</p>
    <div class="divider" style="left:15px;right:31px;top:458px"></div>
    <p class="block copy" style="top:491px">www.bloomiskin.com</p>
    <p class="block heading" style="top:526px;font-size:15.5px">Korean inspired excellence</p>
    <div class="block social" style="top:568px"><span class="social-dot"></span>BLOOMISKIN</div>
    <p class="block distributor" style="top:656px">Distributed by Norvale Labs, Halden, AB T0X 4R2</p>
  </div>
</section>

<section class="wordmarks" aria-label="Wordmark options">
  <h2 class="wordmarks__title">LOGOmark</h2>
  <div class="wordmarks__rule"></div>
  <div class="wordmarks__grid">
    <div class="option">
      <div class="mark mark--inline-right"><span class="mark__name">bloomi<span class="mark__reg">®</span></span><span class="mark__sub">skin</span></div>
      <p class="option__caption">Opt 1</p>
    </div>
    <div class="option">
      <div class="mark mark--inline-left"><span class="mark__name">bloomi<span class="mark__reg">®</span></span><span class="mark__sub">skin</span></div>
      <p class="option__caption">Opt 2</p>
    </div>
    <div class="option">
      <div class="mark mark--stacked"><span class="mark__name">bloomi<span class="mark__reg">®</span></span><span class="mark__sub">skin</span></div>
      <p class="option__caption">Opt 3</p>
    </div>
  </div>
  <div class="wordmarks__rule"></div>
</section>

</body>
</html>
```